Bidwell+ WordPress Design

We need a wordpress design that will incorporate a professional color scheme with company logo in a clean layout. The design needs to consider that this will be developed on a responsive theme. Colors are up to the designer - The red of the logo with black, gray or an accent color (maybe the purple of in the photos). Client wants a 'modern' look.

Industry/Entity Type

It Company

Number of Pages Required

1 page

Font styles to use
Serif
Sans Serif

Requirements
Must have
• Navigation: 1) Home 2) Our Auctions 3) Services 4) Buyers & Sellers 5) About Us 6) Contact Us
• Colors - a corporate look with professional color scheme. Red of logo + black and gray, or any other accent that keeps a corporate look. (purple if it looks good)
• In header - logo (attached) , and contact info
• Phone: 555-304-7261 / 555-618-9042
• eMail: hollisbids@maplewire.example
• bidwellplusregion@maplewire.example
• Address: 6217 W Route 842 • Dunmore, TX 70419
• Design will feature a slideshow either full width (960 px) or in the content area - images attached.
• Widgets in sidebar or where appropriate - 1) Email Signup 2) Upcoming Auctions 4) News&Events blog 5) Testimonials 6) Social media - FB, RSS
• Footer will have company logo, association logos (attached) and contact info, with another widget area if necessary
Nice to have
• Use of dropdown menus:
• 1) News&Events and 2) Testimonials under About Us

```html
<!DOCTYPE html>
<html lang="en">
<head>
<meta charset="utf-8">
<title>Bidwell+ — Auctions</title>
<link rel="stylesheet" href="https://fonts.googleapis.com/css2?family=Roboto:wght@300;400;500;700&display=swap">
<style>
:root{
  --red:#e0161e;
  --purple:#7b2fb5;
  --dark:#232323;
  --text:#333;
  --muted:#555;
  --line:#d6d6d6;
  --footer:#e4e4e4;
  --white:#fff;
}
*{box-sizing:border-box;margin:0;padding:0}
html,body{width:754px;height:1200px;overflow:hidden;background:var(--white)}
body{position:relative;font-family:"Roboto",Arial,sans-serif;color:var(--text)}
.abs{position:absolute}
.brand{font-weight:700;color:var(--dark);font-size:26px;letter-spacing:.5px;display:flex;align-items:center;gap:6px}
.brand .dot{width:10px;height:10px;border-radius:50%;background:var(--red)}
.contact-col{font-size:8px;line-height:14px;color:var(--dark)}
.contact-col h4{font-size:8px;font-weight:500;color:var(--red);margin-bottom:4px;letter-spacing:.3px}
.nav{left:47px;top:79px;width:660px;height:30px;background:var(--dark);display:flex;align-items:center}
.nav a{color:#eee;font-size:7.5px;text-decoration:none;letter-spacing:.3px;position:absolute;top:11px}
.dropdown{left:403px;top:109px;width:82px;height:46px;background:var(--purple);padding:8px 10px;z-index:3}
.dropdown a{display:block;color:#fff;font-size:6.5px;text-decoration:none;line-height:18px;letter-spacing:.3px}
.slider{left:47px;top:109px;width:660px;height:264px;background:linear-gradient(160deg,#6d6a66 0%,#8b8580 35%,#5c4a6e 60%,#a9a49c 100%)}
.dots{left:352px;top:342px;display:flex;gap:6px}
.dots span{width:9px;height:9px;border-radius:50%;background:rgba(255,255,255,.55)}
.dots span.on{background:var(--red)}
.section-title{font-size:13.5px;font-weight:400;color:var(--red);letter-spacing:.3px}
.card{left:47px;width:434px;height:134px;border:1px solid var(--line);border-radius:4px;background:#fff}
.card .thumb{position:absolute;left:13px;top:15px;width:167px;height:99px;border-radius:3px}
.card .info{position:absolute;left:195px;top:15px}
.card .tag{font-size:10px;color:var(--purple);letter-spacing:.3px;margin-bottom:6px}
.card p{font-size:8px;line-height:16px;color:var(--dark);letter-spacing:.2px}
.card p.loc{color:var(--red);font-weight:500}
.btn{display:inline-block;background:var(--dark);color:#fff;font-size:8px;border-radius:4px;text-align:center;letter-spacing:.3px}
.card .btn{margin-top:8px;width:79px;height:26px;line-height:26px}
.widget{left:498px;width:209px;border:1px solid var(--line);border-radius:4px;background:#fff;padding:12px 12px}
.widget h3{font-size:13px;font-weight:400;color:var(--red);letter-spacing:.3px;margin-bottom:8px}
.widget p{font-size:7px;line-height:12.8px;color:var(--muted)}
.widget .btn{height:19px;line-height:19px;padding:0 9px;font-size:8px}
.widget .rule{border-top:1px solid var(--line);margin:10px 0 4px}
.badge{left:209px;top:1008px;width:111px;height:36px;border:1px solid var(--line);border-radius:3px;background:#fff}
.badge span{position:absolute;left:8px;top:7px;width:95px;height:22px;border-radius:10px;background:#dbe3ec}
.footer{left:0;top:1083px;width:754px;height:117px;background:var(--footer)}
.footer h4{font-size:10.5px;font-weight:400;color:var(--red);letter-spacing:.3px}
.footer p{font-size:7.5px;line-height:13.5px;color:var(--muted)}
.seal{border-radius:50%;background:#fff;border:2px solid var(--dark)}
.social{width:22px;height:22px;border-radius:50%}
</style>
</head>
<body>

<header>
  <div class="abs brand" style="left:48px;top:28px"><span>Bidwell+</span><span class="dot"></span></div>
  <div class="abs contact-col" style="left:385px;top:22px"><h4>PHONE</h4>555-304-7261<br>555-618-9042</div>
  <div class="abs contact-col" style="left:478px;top:22px"><h4>EMAIL</h4>hollisbids@maplewire.example<br>bidwellplusregion@maplewire.example</div>
  <div class="abs contact-col" style="left:626px;top:22px"><h4>CONTACT ADDRESS:</h4>6217 W Route 842<br>Dunmore, TX 70419</div>
</header>

<nav class="abs nav">
  <a href="#" style="left:15px">HOME</a>
  <a href="#" style="left:76px">OUR AUCTIONS</a>
  <a href="#" style="left:173px">SERVICES</a>
  <a href="#" style="left:249px">BUYERS &amp; SELLERS</a>
  <a href="#" style="left:361px">ABOUT US</a>
  <a href="#" style="left:438px">CONTACT US</a>
</nav>
<div class="abs dropdown"><a href="#">NEWS &amp; EVENTS</a><a href="#">TESTIMONIALS</a></div>

<div class="abs slider" role="img" aria-label="Slideshow photo of auctioneers in purple shirts calling bids in a warehouse"></div>
<div class="abs dots"><span class="on"></span><span></span><span></span><span></span></div>

<h2 class="abs section-title" style="left:47px;top:395px">OUR AUCTIONS</h2>

<article class="abs card" style="top:421px">
  <div class="thumb" role="img" aria-label="Outdoor lot of items for sale" style="background:linear-gradient(160deg,#8fb7e0 0%,#b58a62 55%,#7a6a4c 100%)"></div>
  <div class="info"><div class="tag">FOR SALE</div><p>5.63 WOODED ACRES LARKMONT, GEORGIA</p><p>(Tolver County)</p><p class="loc">Location:&nbsp; Fennel Road</p><span class="btn">MORE INFO</span></div>
</article>
<article class="abs card" style="top:566px">
  <div class="thumb" role="img" aria-label="Auctioneers working a sale" style="background:linear-gradient(160deg,#8a847d 0%,#6e4f8c 50%,#a8a39a 100%)"></div>
  <div class="info"><div class="tag">FOR SALE</div><p>5.63 WOODED ACRES LARKMONT, GEORGIA</p><p>(Tolver County)</p><p class="loc">Location:&nbsp; Fennel Road</p><span class="btn">MORE INFO</span></div>
</article>
<article class="abs card" style="top:711px">
  <div class="thumb" role="img" aria-label="Room of office furniture and desks" style="background:linear-gradient(160deg,#d8d4cc 0%,#a49480 55%,#6d6158 100%)"></div>
  <div class="info"><div class="tag">FOR SALE</div><p>5.63 WOODED ACRES LARKMONT, GEORGIA</p><p>(Tolver County)</p><p class="loc">Location:&nbsp; Fennel Road</p><span class="btn">MORE INFO</span></div>
</article>
<article class="abs card" style="top:857px">
  <div class="thumb" role="img" aria-label="Farm tractor and equipment under blue sky" style="background:linear-gradient(170deg,#6d9fd6 0%,#b9c9d8 45%,#b53a32 70%,#8a7a63 100%)"></div>
  <div class="info"><div class="tag">FOR SALE</div><p>5.63 WOODED ACRES LARKMONT, GEORGIA</p><p>(Tolver County)</p><p class="loc">Location:&nbsp; Fennel Road</p><span class="btn">MORE INFO</span></div>
</article>

<div class="abs badge" role="img" aria-label="Partner badge"><span></span></div>

<aside>
  <section class="abs widget" style="top:397px;height:222px">
    <h3>UPCOMING AUCTIONS</h3>
    <div role="img" aria-label="Auction team lined up under a tent" style="width:184px;height:91px;border-radius:3px;background:linear-gradient(160deg,#c9c3b6 0%,#6e4f8c 50%,#9b9488 100%);margin-bottom:10px"></div>
    <p>Lorem ipsum dolor sit amet, consect- etuer adipisc-ing elit. Aenean a nibh eget turpis vehicula tempus ac sed massaobortis turpis in odio blandit ac interdum</p>
    <span class="btn" style="margin-top:8px">READ MORE</span>
  </section>

  <section class="abs widget" style="top:629px;height:123px">
    <h3>EMAIL SIGNUP</h3>
    <p style="color:var(--text)">Subscribe below to receive alerts on<br>Upcoming Auctions. It’s Free!</p>
    <div style="margin-top:6px;height:23px;border:1px solid var(--line);border-radius:4px;font-size:7px;color:#888;padding:7px 10px">Email Address</div>
    <div style="text-align:right;margin-top:5px"><span class="btn" style="background:var(--purple);padding:0 17px">SIGN UP</span></div>
  </section>

  <section class="abs widget" style="top:758px;height:146px">
    <h3>NEWS AND UPDATES</h3>
    <div style="font-size:8px;color:var(--purple);margin:4px 0 2px;letter-spacing:.2px">NAM FERMENTUM VESTIBULUM</div>
    <p>Lorem ipsum dolor sit amet, consect- etuer adipiscing elit. Aenean a nibh eget turpis vehicula tempus ac sed massa.</p>
    <div style="font-size:7px;color:var(--dark);margin-top:4px">READ MORE</div>
    <div class="rule"></div>
    <div style="text-align:right"><span class="btn" style="padding:0 13px">READ ALL</span></div>
  </section>

  <section class="abs widget" style="top:915px;height:146px">
    <h3>TESTIMONIALS</h3>
    <p style="font-style:italic">“ Lorem ipsum dolor sit amet, consect- etuer adipiscing elit. Aenean a nibh eget turpis vehicula tempus ac sed massaobortis turpis in odio blandit ac interdum..”</p>
    <div style="font-size:7px;color:var(--purple);margin-top:8px">-NAME HEADING</div>
    <div class="rule" style="margin-top:14px"></div>
    <div style="text-align:right"><span class="btn" style="padding:0 13px">READ ALL</span></div>
  </section>
</aside>

<footer class="abs footer">
  <div class="abs brand" style="left:47px;top:30px;font-size:18px"><span>Bidwell+</span><span class="dot" style="width:7px;height:7px"></span></div>
  <p class="abs" style="left:47px;top:73px">Copyright © 2015 Bidwell+<br>All Rights Reserved.</p>

  <h4 class="abs" style="left:215px;top:18px">ASSOCIATION</h4>
  <div class="abs seal" role="img" aria-label="State association badge" style="left:216px;top:38px;width:46px;height:46px"></div>
  <div class="abs" role="img" aria-label="National association badge" style="left:278px;top:40px;width:40px;height:42px;background:var(--dark);border-radius:3px"></div>

  <h4 class="abs" style="left:385px;top:18px">CONTACT INFO</h4>
  <p class="abs" style="left:385px;top:36px">6217 W Route 842<br>Dunmore, TX 70419<br>555-304-7261 / 555-618-9042<br>hollisbids@maplewire.example<br>bidwellplusregion@maplewire.example</p>

  <h4 class="abs" style="left:573px;top:18px">CONNECT US</h4>
  <div class="abs social" role="img" aria-label="Social profile" style="left:574px;top:41px;background:#3b5998"></div>
  <div class="abs social" role="img" aria-label="News feed" style="left:603px;top:41px;background:#f26522"></div>
</footer>

</body>
</html>
```